Flyer Design for catering company "Marlow's Pantry"

We need a flyer design for a small catering company based in Melbourne, Australia called Marlow's Pantry. We are in the process of re-branding at the moment and want to use the new brand for the logo. The new website is still under development but you can have a look at it here: http://marlowspantry.exampleweb.com/minimal-layout The product we want to market i the flyer are our ready-made meals. We are marketing to the corporate world. The meals are intended to be purchased by large firms to feed their staff that are working back late after-hours. They are home-made, fresh, healthy, convenient and most importantly - delicious! You can find the menu and a brief explanation of the ready-made meals on the website. I thought that we might include the menu on the backside of the flyer but i am not set on this.

We want to provide an introductory offer of 10 meals for $100 (usually $130).

I have attached an image of where i got to with the flyer just for your information. You can see why i need your assistance!
Updates

I should also add that the logo is intended to be printed in a gold foil! Added Wednesday, February 3, 2016

Target Market(s)

Corporate market - this doesnt mean boring though. It wont be the big bosses who read this flyer it will be the catering managers - they are likely to see a lot of flyers so this one needs to stand out.

Industry/Entity Type

Catering

Requirements
Must have
• Must have the logo! Keep in mind the logo will be printed in a gold foil so it will be very metallic.
• Must reference introductory offer of 10 meals for $100.
• Must have website.
Nice to have
• Would like to see the menu on the backside - i am flexible with this if you have a better idea.
Should not have
• no cartoony images

```html
<!DOCTYPE html>
<html lang="en">
<head>
<meta charset="utf-8">
<title>Marlow's Pantry – Traditional Dishes</title>
<link rel="stylesheet" href="https://fonts.googleapis.com/css2?family=Arimo:wght@400;700&family=Josefin+Sans:wght@300&display=swap">
<style>
  :root {
    --paper: #ffffff;
    --band-grey: #cccccc;
    --footer-grey: #d2d2d2;
    --ink: #111111;
    --heading-ink: #1e1e1e;
    --gold: #c9a449;
    --gold-light: #e2c97a;
    --photo-warm: #b9a58a;
    --photo-cool: #8c8a86;
    --rule: #8a8a8a;
  }
  * { margin: 0; padding: 0; box-sizing: border-box; }
  html, body { width: 847px; height: 1200px; overflow: hidden; background: var(--paper); }
  .flyer {
    position: relative;
    width: 847px;
    height: 1200px;
    background: var(--paper);
    font-family: "Arimo", Arial, sans-serif;
    color: var(--ink);
    overflow: hidden;
  }
  .header-photo {
    position: absolute; left: 0; top: 0; width: 847px; height: 111px;
    background: linear-gradient(90deg, var(--photo-cool) 0%, var(--photo-warm) 25%, #d6cbbb 50%, var(--photo-warm) 75%, var(--photo-cool) 100%);
  }
  .title-band {
    position: absolute; left: 0; top: 111px; width: 847px; height: 104px;
    background: var(--band-grey);
  }
  .page-title {
    position: absolute; left: 347px; top: 134px;
    font-family: "Josefin Sans", "Century Gothic", sans-serif;
    font-weight: 300; font-size: 38px; letter-spacing: 0;
    color: var(--heading-ink); text-transform: uppercase; white-space: nowrap;
  }
  .intro-offer {
    position: absolute; left: 349px; top: 184px;
    font-size: 14px; font-weight: 700; color: var(--heading-ink); white-space: nowrap;
  }
  .brand-mark {
    position: absolute; left: 129px; top: 63px; width: 164px; height: 164px;
    border-radius: 50%;
    background: var(--gold);
    display: flex; align-items: center; justify-content: center; text-align: center;
  }
  .brand-name {
    font-family: "Arimo", Arial, sans-serif;
    font-weight: 700; font-size: 22px; line-height: 1.2; color: var(--paper);
  }
  .dish {
    position: absolute; left: 142px; width: 600px;
    font-size: 17px; line-height: 21.7px;
  }
  .dish-name { font-weight: 700; }
  .intro-note { font-weight: 400; }
  .divider {
    position: absolute; left: 142px; top: 1027px; width: 600px;
    border-top: 1px dotted var(--rule);
  }
  .contact {
    position: absolute; left: 142px; top: 1052px;
    font-size: 17px; line-height: 28px;
  }
  .contact .phone { font-weight: 700; }
  .social {
    position: absolute; left: 616px; top: 1069px;
    display: flex; gap: 20px;
  }
  .social span {
    width: 34px; height: 34px; border-radius: 50%; background: var(--ink); display: block;
  }
  .footer-band {
    position: absolute; left: 0; top: 1168px; width: 847px; height: 32px;
    background: var(--footer-grey);
  }
  .visit-tab {
    position: absolute; left: 567px; top: 1134px; width: 235px; height: 36px;
    background: linear-gradient(180deg, var(--gold-light), var(--gold));
    border-radius: 6px 6px 14px 14px;
    transform: rotate(2deg);
    font-size: 12px; color: var(--heading-ink);
    display: flex; align-items: center; justify-content: center;
  }
</style>
</head>
<body>
<div class="flyer">
  <div class="header-photo" role="img" aria-label="Photograph of fresh bagels and packed meal containers"></div>
  <div class="title-band"></div>
  <div class="brand-mark"><span class="brand-name">Marlow's<br>Pantry</span></div>
  <h1 class="page-title">Traditional Dishes</h1>
  <p class="intro-offer">Introductory offer: 10 meals for $100 (usually $130)</p>

  <div class="dish" style="top:266px"><div class="dish-name">Traditional lasagne</div><div>Beef lasagne with a creamy béchamel sauce</div></div>
  <div class="dish" style="top:331px"><div class="dish-name">Pork and veal meatballs</div><div>Pork &amp; veal meatballs in a rich tomato passata with risoni &amp; green beans</div></div>
  <div class="dish" style="top:396px"><div class="dish-name">Thai red beef curry</div><div>Slow cooked red beef curry with basmati rice</div></div>
  <div class="dish" style="top:461px"><div class="dish-name">Spinach &amp; ricotta cannelloni (Vegetarian)</div><div>Spinach, ricotta &amp; pumpkin cannelloni with a rich tomato passata</div></div>
  <div class="dish" style="top:526px"><div class="dish-name">Chicken risotto (Gluten Free)</div><div>Traditional risotto made with chicken, fresh vegetables and Arborio rice</div></div>
  <p class="dish intro-note" style="top:588px">HEALTHY OPTIONS – All of our home made meals are good for you, but these meals are designed for the health conscious among us!</p>
  <div class="dish" style="top:659px"><div class="dish-name">Shepherd’s pie (Gluten Free)</div><div>A low carb version of the classic British dish made with minced lamb and covered with a delicious sweet potato and potato mash</div></div>
  <div class="dish" style="top:744px"><div class="dish-name">Chicken cattiatore (Gluten Free)</div><div>An Italian dish of chicken braised in a tomato-based sauce with olives, herbs and vegetables and served on a bed of sweet potato and pumpkin mash</div></div>
  <div class="dish" style="top:853px"><div class="dish-name">Chickpea &amp; pumpkin yellow curry (Vegetarian, Gluten Free)</div><div>A fragrant yet milk yellow curry made with chickpeas, pumpkin and spinach, served on a bed of brown rice</div></div>
  <div class="dish" style="top:938px"><div class="dish-name">Moroccan vegetable tagine (Vegetarian)</div><div>A traditional Moroccan stew made with a variety of fresh vegetables and served on a bed of wholemeal cous cous</div></div>

  <div class="divider"></div>
  <div class="contact">
    <div class="phone">P: 0400 512 687</div>
    <div>E: hello@marlowspantry.com.au</div>
    <div>A: 42 Harbour Lane, Port Melbourne VIC 3207</div>
  </div>
  <div class="social" aria-label="Social media links"><span></span><span></span><span></span></div>

  <div class="footer-band"></div>
  <div class="visit-tab">Visit :www.marlowspantry.com.au</div>
</div>
</body>
</html>
```